Website for a Pittsburgh Musical Production

We are creating a website for a musical stage production. Content and copy is included below. We are targeting production in early 2023.

Coded - Design and coding required

1 page

```html
<!DOCTYPE html>
<html lang="en">
<head>
<meta charset="utf-8">
<title>Ironhollow The Rock Opera</title>
<link rel="stylesheet" href="https://fonts.googleapis.com/css2?family=Lato:wght@400;700;900&display=swap">
<style>
:root{
  --page:#222222;
  --card:#111111;
  --black:#000000;
  --green:#679a43;
  --green-text:#7fae55;
  --text:#e6e6e6;
  --muted:#cfcfcf;
  --white:#ffffff;
  --band-dark:#1b1b1b;
}
*{margin:0;padding:0;box-sizing:border-box}
html,body{width:1200px;height:3986px;overflow:hidden}
body{background:var(--page);font-family:'Lato',sans-serif;color:var(--text)}
.hero{position:relative;height:711px;background:linear-gradient(100deg,#3f4d2a 0%,#2b3320 30%,#1c1f16 55%,#151712 100%)}
.hero-art{position:absolute;left:0;top:0;width:520px;height:711px;background:radial-gradient(ellipse at 40% 45%,#7f9e54 0%,#4b5d31 45%,rgba(30,36,20,0) 80%)}
.hero-title{position:absolute;right:66px;top:225px;text-align:right}
.hero-title .name{font-size:96px;font-weight:700;color:#6f8f45;line-height:1}
.hero-title .tag{font-size:40px;font-weight:700;color:#6f8f45;margin-top:6px}
.nav{height:67px;background:var(--black);display:flex;justify-content:center;align-items:center;gap:40px}
.nav a{color:var(--white);text-decoration:none;font-size:13px;font-weight:700;text-transform:uppercase}
.nav a.active{color:var(--green-text)}
.welcome{height:439px;text-align:center;padding-top:50px}
.section-title{font-size:34px;font-weight:700;color:var(--white);text-transform:uppercase;line-height:46px}
.welcome p{width:870px;margin:24px auto 0;font-size:15.5px;line-height:31px;color:var(--muted)}
.btn{display:inline-block;background:var(--green);color:var(--white);font-weight:700;font-size:17px;text-transform:uppercase;text-decoration:none;width:179px;height:52px;line-height:52px;text-align:center}
.welcome .btn{margin-top:30px}
.feature{position:relative;height:563px;background:var(--black);overflow:hidden}
.feature-photo{position:absolute;left:280px;top:0;right:0;bottom:0}
.feature-photo.concert{background:linear-gradient(90deg,#000 0%,#2a1a12 25%,#5a3a26 55%,#6b4a33 75%,#3a2a20 100%)}
.feature-photo.band{background:linear-gradient(90deg,#000 0%,#141a3a 25%,#2d2a5a 50%,#4a2840 70%,#1a1f40 100%)}
.feature-copy{position:absolute;left:74px;top:106px;width:600px}
.feature-copy h2{font-size:86px;font-weight:900;color:var(--white);line-height:82px;text-transform:uppercase}
.feature-copy p{font-size:15.5px;line-height:31px;color:var(--muted);margin-top:14px;width:575px}
.feature-copy .btn{margin-top:22px}
.events{height:556px;padding-top:62px}
.events .section-title{text-align:center}
.cards{display:flex;gap:28px;margin:44px 0 0 74px}
.card{width:243px;height:328px;background:var(--card)}
.card-photo{height:173px}
.card-body{padding:18px 19px}
.card-date{font-size:14px;color:var(--green-text)}
.card-title{font-size:14px;font-weight:700;color:var(--white);text-transform:uppercase;margin-top:12px}
.card-text{font-size:14px;line-height:22px;color:var(--muted);margin-top:12px}
.gallery{height:646px;padding-top:48px}
.gallery .section-title{text-align:center}
.grid{display:grid;grid-template-columns:repeat(4,262px);grid-template-rows:repeat(2,223px);gap:2px;margin:36px 0 0 74px}
.subscribe{height:258px;background:var(--band-dark);text-align:center;padding-top:48px}
.subscribe p{font-size:15px;color:var(--muted);margin-top:8px}
.subscribe-form{width:567px;height:61px;margin:24px auto 0;background:var(--white);display:flex;align-items:center;justify-content:space-between;padding:0 10px 0 20px}
.subscribe-form span{font-size:13px;color:#333}
.subscribe-form .btn{width:145px;height:44px;line-height:44px;font-size:17px}
.footer{height:183px;background:var(--black);text-align:center;padding-top:40px}
.footer .nav{height:auto}
.copyright{font-size:14px;color:var(--muted);margin-top:20px}
.social{display:flex;justify-content:center;gap:26px;margin-top:16px}
.social span{width:16px;height:16px;border-radius:50%;background:var(--white)}
</style>
</head>
<body>
<header class="hero">
  <div class="hero-art" role="img" aria-label="Dark green sketched artwork with rough ink strokes"></div>
  <div class="hero-title">
    <div class="name">Ironhollow</div>
    <div class="tag">the rock opera</div>
  </div>
</header>
<nav class="nav">
  <a class="active" href="#">Home</a><a href="#">About Us</a><a href="#">Services</a><a href="#">Upcoming Events</a><a href="#">Tours</a><a href="#">Blog</a><a href="#">Gallery</a><a href="#">Contact</a>
</nav>
<section class="welcome">
  <h1 class="section-title">Welcome to<br>Ironhollow The Rock Opera</h1>
  <p>Sed ut perspiciatis unde omnis iste natus error sit voluptatem accusantium doloremque laudantium, totam rem aperiam, eaque ipsa quae ab illo inventore veritatis et quasi architecto beatae vitae dicta sunt explicabo. Nemo enim ipsam voluptatem quia voluptas sit aspernatur aut odit aut fugit, sed quia consequuntur magni dolores eos qui ratione voluptatem sequi nesciunt.</p>
  <a class="btn" href="#">Read More</a>
</section>
<section class="feature">
  <div class="feature-photo concert" role="img" aria-label="Singer in a white gown beside a grand piano in a concert hall"></div>
  <div class="feature-copy">
    <h2>Rock Opera<br>Concert</h2>
    <p>Sed ut perspiciatis unde omnis iste natus error sit voluptatem accusantium doloremque laudantium, totam rem aperiam, eaque ipsa quae ab illo inventore veritatis et quasi architecto beatae.</p>
    <a class="btn" href="#">Read More</a>
  </div>
</section>
<section class="events">
  <h2 class="section-title">Upcoming Events</h2>
  <div class="cards">
    <article class="card"><div class="card-photo" role="img" aria-label="Two singers performing a duet" style="background:linear-gradient(135deg,#6a5a4e,#3a2c2a)"></div><div class="card-body"><div class="card-date">APR 20, 2021</div><div class="card-title">Quis autem vel eum iure</div><div class="card-text">Sed ut perspiciatis unde omnis iste natus.</div></div></article>
    <article class="card"><div class="card-photo" role="img" aria-label="Singers on a lit stage" style="background:linear-gradient(180deg,#2a3a6a,#5a4a6a)"></div><div class="card-body"><div class="card-date">APR 20, 2021</div><div class="card-title">Quis autem vel eum iure</div><div class="card-text">Sed ut perspiciatis unde omnis iste natus.</div></div></article>
    <article class="card"><div class="card-photo" role="img" aria-label="Rock band under purple stage lights" style="background:linear-gradient(135deg,#5a3a9a,#1a1a4a)"></div><div class="card-body"><div class="card-date">APR 20, 2021</div><div class="card-title">Quis autem vel eum iure</div><div class="card-text">Sed ut perspiciatis unde omnis iste natus.</div></div></article>
    <article class="card"><div class="card-photo" role="img" aria-label="Audience in a concert hall with red curtain" style="background:linear-gradient(180deg,#7a1a1a,#3a2a26)"></div><div class="card-body"><div class="card-date">APR 20, 2021</div><div class="card-title">Quis autem vel eum iure</div><div class="card-text">Sed ut perspiciatis unde omnis iste natus.</div></div></article>
  </div>
</section>
<section class="feature">
  <div class="feature-photo band" role="img" aria-label="Jazz band with singer, double bass and saxophone"></div>
  <div class="feature-copy">
    <h2>Rock Opera<br>Band</h2>
    <p>Sed ut perspiciatis unde omnis iste natus error sit voluptatem accusantium doloremque laudantium, totam rem aperiam, eaque ipsa quae ab illo inventore veritatis et quasi architecto beatae.</p>
    <a class="btn" href="#">View Our Team</a>
  </div>
</section>
<section class="gallery">
  <h2 class="section-title">Photo Gallery</h2>
  <div class="grid">
    <div role="img" aria-label="Singer in black dress on dark stage" style="background:linear-gradient(135deg,#1a1a1a,#3a3434)"></div>
    <div role="img" aria-label="Performers on stage in smoke and lights" style="background:linear-gradient(135deg,#8a8a92,#4a2a30)"></div>
    <div role="img" aria-label="Singers on a lit stage" style="background:linear-gradient(180deg,#2a3a6a,#5a4a6a)"></div>
    <div role="img" aria-label="Singer against a pink background" style="background:linear-gradient(135deg,#e8a8b8,#c88898)"></div>
    <div role="img" aria-label="Singer in white gown beside a piano" style="background:linear-gradient(135deg,#5a3a26,#2a1a12)"></div>
    <div role="img" aria-label="Singer and bassist under blue light" style="background:linear-gradient(135deg,#2a2a5a,#5a2a4a)"></div>
    <div role="img" aria-label="Two singers performing a duet" style="background:linear-gradient(135deg,#6a5a4e,#3a2c2a)"></div>
    <div role="img" aria-label="String players in an orchestra" style="background:linear-gradient(135deg,#3a2a22,#7a4a2a)"></div>
  </div>
</section>
<section class="subscribe">
  <h2 class="section-title">Email Subscribe</h2>
  <p>Sed ut perspiciatis unde omnis iste natus error sit voluptatem accusantium doloremque laudantium.</p>
  <div class="subscribe-form"><span>Enter Email Address</span><a class="btn" href="#">Subscribe</a></div>
</section>
<footer class="footer">
  <nav class="nav">
    <a href="#">Home</a><a href="#">About Us</a><a href="#">Services</a><a href="#">Upcoming Events</a><a href="#">Tours</a><a href="#">Blog</a><a href="#">Gallery</a><a href="#">Contact</a>
  </nav>
  <div class="copyright">Copyright © 2021 Company Name All Rights Reserved</div>
  <div class="social"><span></span><span></span><span></span><span></span></div>
</footer>
</body>
</html>
```